Harbor Ridge Capital and Investments

Create a simple business card design using the logos attached. Make it similar but not exact to the reference photo. Brand guidelines are also included.

```html
<!DOCTYPE html>
<html lang="en">
<head>
<meta charset="UTF-8">
<title>Harbor Ridge Capital – Business Card</title>
<link rel="stylesheet" href="https://fonts.googleapis.com/css2?family=Montserrat:wght@400;500;700&display=swap">
<style>
  :root {
    --navy: #1f2845;
    --copper: #b25b24;
    --paper: #ffffff;
    --ink: #2a2f3d;
    --backdrop: #e4e5e8;
  }
  * { box-sizing: border-box; margin: 0; padding: 0; }
  html, body { width: 1200px; height: 915px; overflow: hidden; }
  body {
    background: var(--backdrop);
    font-family: "Montserrat", sans-serif;
    position: relative;
  }
  .card {
    position: absolute;
    width: 560px;
    height: 320px;
    border-radius: 18px;
    overflow: hidden;
    box-shadow: 0 6px 18px rgba(0,0,0,0.18);
  }
  .card-back {
    left: 70px; top: 110px;
    background: var(--navy);
    display: flex; align-items: center; justify-content: center;
  }
  .card-front {
    left: 570px; top: 485px;
    background: var(--paper);
  }
  .brand {
    display: flex; align-items: center; gap: 12px;
    font-weight: 700; letter-spacing: 1px; text-transform: uppercase;
  }
  .brand-mark { width: 16px; height: 16px; border-radius: 50%; flex: none; }
  .card-back .brand { color: var(--paper); font-size: 30px; }
  .card-back .brand-mark { background: var(--paper); }
  .card-front .brand {
    position: absolute; left: 28px; top: 120px; width: 230px;
    color: var(--navy); font-size: 22px; line-height: 1.2;
  }
  .card-front .brand-mark { background: var(--copper); }
  .divider {
    position: absolute; left: 275px; top: 40px;
    width: 2px; height: 170px; background: var(--copper);
  }
  .details {
    position: absolute; left: 300px; top: 36px;
    color: var(--ink); font-size: 12.5px; line-height: 1.45;
  }
  .person-name { color: var(--copper); font-weight: 700; font-size: 19px; letter-spacing: 0.3px; }
  .person-role { margin-bottom: 10px; }
  .address { margin-bottom: 10px; }
  .contact-line { display: flex; align-items: center; gap: 8px; }
  .contact-line svg { width: 12px; height: 12px; flex: none; }
  .footer-bands { position: absolute; left: 0; bottom: 0; width: 560px; height: 90px; }
  .website {
    position: absolute; right: 22px; bottom: 56px;
    color: var(--paper); font-size: 12.5px; letter-spacing: 0.3px;
  }
</style>
</head>
<body>

<section class="card card-back">
  <div class="brand"><span class="brand-mark"></span>Harbor Ridge Capital</div>
</section>

<section class="card card-front">
  <div class="brand"><span class="brand-mark"></span>Harbor Ridge Capital</div>
  <div class="divider"></div>

  <div class="details">
    <div class="person-name">MAREN ELLSWORTH</div>
    <div class="person-role">Managing Director</div>
    <div class="address">Your address, City<br>State, Zip 1234</div>
    <div class="contact-line">
      <svg viewBox="0 0 12 12" aria-hidden="true"><path d="M2.5 1h2l1 3-1.3 1a6 6 0 0 0 2.8 2.8L8 6.5l3 1v2A1.5 1.5 0 0 1 9.5 11 8.5 8.5 0 0 1 1 2.5 1.5 1.5 0 0 1 2.5 1z" fill="var(--copper)"/></svg>
      123 456 789
    </div>
    <div class="contact-line">
      <svg viewBox="0 0 12 12" aria-hidden="true"><rect x="3" y="0.8" width="6" height="10.4" rx="1" fill="none" stroke="var(--copper)" stroke-width="1.2"/><circle cx="6" cy="9.4" r="0.6" fill="var(--copper)"/></svg>
      123 456 789
    </div>
    <div class="contact-line">
      <svg viewBox="0 0 12 12" aria-hidden="true"><rect x="0.5" y="2.5" width="11" height="7.5" fill="var(--copper)"/><path d="M0.8 2.8 6 7l5.2-4.2" fill="none" stroke="#fff" stroke-width="1"/></svg>
      info@harborridgecapital.com
    </div>
  </div>

  <svg class="footer-bands" viewBox="0 0 560 90" preserveAspectRatio="none" aria-hidden="true">
    <polygon points="0,72 360,72 372,60 560,60 560,90 0,90" fill="var(--navy)"/>
    <polygon points="0,62 356,62 370,48 560,48 560,54 374,54 360,68 0,68" fill="var(--copper)"/>
    <polygon points="380,40 560,40 560,46 374,46" fill="var(--copper)" opacity="0"/>
  </svg>
  <div class="website" style="bottom:8px;">www.harborridgecapital.com</div>
</section>

</body>
</html>
```